Wordpress Design Project (Millbrook)

We need a wordpress design for an established auction and real estate company based in California. The winning design will incorporate a creative layout, pleasing color scheme and logo in a very professional and clean manner.

Industry/Entity Type

Real Estate

Requirements
Must have
• Client likes the overall look of http://vornpeq.com/. Site will use the logo colors and maybe complimentary highlight color. Note from client: "“It's important that the appearance of the site will be unique and easily recognizable. In general try to avoid too many colors especially bright and negative contention colors such as bright red, orange, yellow and such. "

The layout should be close as the mentioned reference site except the slideshow (image attached) should be placed below navigation, perhaps at top of content area for the page. Sidebar widgets will include:
- SMS signup form
- Register to bid call to action (as in reference site)
- Email signup form (with only "enter email" field)
- Blog feature "News & Events"
- Social media icons for facebook, twitter, google+, RSS

Navigation:
1) Home
2) Auctions
3) Online Auctions
4) Past Auctions
5) About Us
6) FAQ
7) Blog
8) Contact Us
Nice to have
• Site will have drop-down menus, idea of these would be nice for any of the primary navigation tabs.
Should not have
• please use no auction gavels in the design

```html
<!DOCTYPE html>
<html lang="en">
<head>
<meta charset="utf-8">
<title>Millbrook Auctions</title>
<link rel="stylesheet" href="https://fonts.googleapis.com/css2?family=Arimo:wght@400;700&family=Tinos:wght@400;700&display=swap">
<style>
:root{
  --teal-dark:#0f4f45;
  --teal:#1a6b5f;
  --teal-light:#2a8a7b;
  --teal-text:#17695c;
  --brick:#b5604a;
  --brick-dark:#93442f;
  --ink:#222;
  --page-top:#2aa0a6;
  --page-bottom:#8d8d8d;
  --card-bg:#f2f2f2;
  --line:#d6d6d6;
}
*{box-sizing:border-box;margin:0;padding:0}
html,body{width:1200px;height:1198px;overflow:hidden}
body{position:relative;font-family:"Arimo",Arial,sans-serif;color:var(--ink);
  background:linear-gradient(180deg,var(--page-top) 0,#6cb8bc 160px,#c9d3d3 330px,#b4b4b4 700px,var(--page-bottom) 1198px)}
.abs{position:absolute}
.sheet{left:103px;top:15px;width:994px;height:994px;background:#fff;border-radius:4px}
.nav{left:109px;top:20px;width:979px;height:50px;border-radius:6px;
  background:linear-gradient(180deg,#1f7a6c,var(--teal-dark));display:flex;align-items:center;padding-left:8px}
.nav a{font-family:"Tinos",serif;color:#fff;text-decoration:none;font-size:15px;padding:0 22px;position:relative;height:50px;line-height:50px}
.nav a+a::before{content:"";position:absolute;left:0;top:15px;height:20px;border-left:1px solid #3d8f82}
.nav a.open::after{content:"";position:absolute;left:50%;bottom:5px;margin-left:-4px;border:4px solid transparent;border-top-color:#fff}
.dropdown{left:503px;top:71px;width:158px;height:139px;background:var(--teal-dark);border-radius:0 0 6px 6px;padding-top:8px}
.dropdown a{display:block;margin:0 5px 8px;height:24px;line-height:22px;padding-left:14px;color:#fff;font-size:14px;text-decoration:none;border-radius:5px}
.dropdown a.active{background:#b9615a}
.logo{left:115px;top:100px;width:276px;height:110px;display:flex;align-items:center;justify-content:center;gap:10px}
.logo .mark{width:22px;height:22px;background:var(--teal)}
.logo span{font-family:"Tinos",serif;font-size:30px;color:var(--teal);letter-spacing:1px}
.alerts{left:114px;top:223px;width:279px;height:142px;border-radius:6px;background:linear-gradient(180deg,#1c7466,var(--teal-dark))}
.alerts h2{position:absolute;left:12px;top:12px;font-family:"Tinos",serif;font-size:21px;color:#fff}
.field{position:absolute;background:linear-gradient(180deg,#fff,#e9e9e9);border-radius:5px;font-size:12px;color:#333;padding-left:9px;display:flex;align-items:center}
.btn-dark{position:absolute;border-radius:6px;background:linear-gradient(180deg,#555,#111);color:#fff;font-weight:700;font-size:19px;display:flex;align-items:center;justify-content:center;gap:10px}
.photo{border-radius:6px}
.slide{left:407px;top:89px;width:325px;height:276px;background:linear-gradient(135deg,#6b3a22,#a67a4e 45%,#4a2a18)}
.video{left:742px;top:88px;width:341px;height:279px;border:1px solid var(--line);background:#fff}
.video .screen{position:absolute;left:6px;top:6px;width:329px;height:260px;background:linear-gradient(180deg,#e6e6e6,#c9c9c9)}
.video .play{position:absolute;left:129px;top:87px;width:84px;height:60px;background:#222;border-radius:4px}
.video .bar{position:absolute;left:11px;top:243px;width:319px;height:24px;background:#111;color:#fff;font-size:11px;display:flex;align-items:center;padding:0 8px;gap:10px}
.bar .track{flex:1;height:4px;background:#555;border-radius:2px}
.section-title{left:114px;top:401px;font-size:18px;color:#222}
.card{width:664px;height:270px;border:1px solid var(--line);border-radius:5px;background:linear-gradient(180deg,#fff,var(--card-bg))}
.card .head{height:38px;background:linear-gradient(180deg,#1f7a6c,var(--teal-dark));border-radius:4px 4px 0 0;color:#fff;font-weight:700;font-size:15px;line-height:38px;padding-left:10px;letter-spacing:.3px}
.card .thumb{position:absolute;left:12px;top:70px;width:149px;height:104px;border:1px solid #2b5fa6;background:linear-gradient(180deg,#9fc3e6 0,#c4d4dc 40%,#5f8a3a 75%,#3f6b2a)}
.card .title{position:absolute;left:183px;top:70px;width:470px;color:var(--teal-text);font-weight:700;font-size:14px;line-height:18px;letter-spacing:.3px}
.card .info{position:absolute;left:184px;top:112px;font-size:13.5px;line-height:15.7px}
.details{position:absolute;left:11px;top:191px;width:150px;height:37px;border-radius:7px;background:linear-gradient(180deg,#c66e55,var(--brick-dark));color:#fff;font-weight:700;font-size:17px;display:flex;align-items:center;justify-content:center;gap:10px}
.card .bid{position:absolute;left:185px;top:200px;font-size:13.5px;line-height:20px}
.card .bid b{color:var(--teal-text);font-size:13px}
.register{left:803px;top:383px;width:280px;height:199px;border:1px solid var(--line);border-radius:6px;background:linear-gradient(180deg,#fff,#e8f6f8);text-align:center}
.register h2{font-family:"Tinos",serif;font-size:29px;color:var(--teal-text);margin-top:10px;letter-spacing:.5px}
.register p{font-size:16px;line-height:19px;margin-top:2px}
.register .art{position:absolute;left:50px;top:95px;width:180px;height:98px;border-radius:6px;background:radial-gradient(ellipse at 45% 40%,#c2503c 0,#d98a74 35%,#e8f6f8 75%)}
.house-box{left:804px;top:607px;width:278px;height:178px;border:1px solid var(--line);border-radius:6px;background:#fff}
.house-box .img{position:absolute;left:7px;top:7px;width:263px;height:162px;background:linear-gradient(180deg,#5aa6e0 0,#a9d0ee 35%,#d9cdb8 55%,#6f9a4a 85%)}
.sms{left:801px;top:806px;width:280px;height:188px;border-radius:6px;background:linear-gradient(180deg,#bd6650,var(--brick-dark))}
.sms h2{position:absolute;left:15px;top:12px;font-family:"Tinos",serif;font-size:21px;color:#fff}
.footer{left:101px;top:1044px;width:996px;height:112px;border-radius:6px;background:linear-gradient(180deg,#1f7a6c,var(--teal-dark));color:#fff;font-size:12.5px}
.footer .flogo{position:absolute;left:18px;top:40px;display:flex;align-items:center;gap:8px}
.footer .flogo .mark{width:16px;height:16px;background:#d9ece7}
.footer .flogo span{font-family:"Tinos",serif;font-size:22px;color:#d9ece7}
.footer .links{position:absolute;left:294px;top:29px;word-spacing:1px}
.footer .links i{font-style:normal;margin:0 8px}
.footer .line{position:absolute;width:996px;left:122px;text-align:center;width:870px;left:0;padding-left:244px}
</style>
</head>
<body>
<div class="abs sheet"></div>

<nav class="abs nav">
  <a>HOME</a><a>AUCTIONS</a><a>ONLINE AUCTIONS</a><a class="open">PAST AUCTIONS</a><a>ABOUT US</a><a>FAQ</a><a>BLOG</a><a>CONTACT US</a>
</nav>

<div class="abs logo"><div class="mark"></div><span>Millbrook Auctions</span></div>

<div class="abs slide photo" role="img" aria-label="Antique shop interior with a glass cabinet and wooden furniture"></div>

<div class="abs dropdown">
  <a>Past Auction #</a><a class="active">Past Auction #</a><a>Past Auction #</a><a>Past Auction #</a>
</div>

<section class="abs alerts">
  <h2>Sign up for Auction Alerts</h2>
  <div class="field" style="left:12px;top:52px;width:246px;height:34px">Enter your email</div>
  <div class="btn-dark" style="left:54px;top:96px;width:151px;height:37px">
    <svg width="32" height="22" viewBox="0 0 32 22"><rect x="1" y="1" width="30" height="20" rx="2" fill="#eee"/><path d="M1 2l15 11L31 2" stroke="#555" stroke-width="2" fill="none"/></svg>Join Now
  </div>
</section>

<div class="abs video">
  <div class="screen" role="img" aria-label="Video preview frame">
    <div class="play"><svg width="84" height="60" viewBox="0 0 84 60"><path d="M33 14l22 16-22 16z" fill="#fff"/></svg></div>
  </div>
  <div class="bar">
    <svg width="10" height="10" viewBox="0 0 10 10"><path d="M2 1l7 4-7 4z" fill="#fff"/></svg>
    <span>00:00</span><div class="track"></div><span>00:00</span>
    <svg width="30" height="10" viewBox="0 0 30 10"><path d="M0 3h3l3-3v10l-3-3H0z" fill="#fff"/><path d="M10 8h1M13 7h1v3M16 6h1v4M19 5h1v5M22 4h1v6M25 2h1v8" stroke="#fff"/></svg>
    <svg width="12" height="12" viewBox="0 0 12 12"><path d="M1 4V1h3M8 1h3v3M11 8v3H8M4 11H1V8" stroke="#fff" fill="none"/></svg>
  </div>
</div>

<h2 class="abs section-title">CURRENT &amp; UPCOMING AUCTIONS</h2>

<article class="abs card" style="left:115px;top:433px">
  <div class="head">HALDEN WELLNESS CENTER IN ASHGROVE, GA</div>
  <div class="thumb" role="img" aria-label="Large two-story house with lawn"></div>
  <div class="title">Corwin Tate Auctions, LLC GAL 5812 - Everything sold to the high bidder</div>
  <div class="info">Location:<br>Location 1 - 418 Maple Ridge Rd<br>Location 2 - 52 Cedar Hollow # 3<br>Ashgrove, GA 30999</div>
  <div class="details"><svg width="24" height="24" viewBox="0 0 24 24"><rect x="1" y="1" width="17" height="20" rx="2" fill="#fff"/><circle cx="10" cy="11" r="5" fill="none" stroke="#b5604a" stroke-width="2"/><path d="M14 15l7 7" stroke="#fff" stroke-width="3"/></svg>DETAILS</div>
  <div class="bid"><b>Online Bidding Only</b><br>Began:&nbsp; Friday, May 24, 2013 at 10:06 AM EDT<br>Ends:&nbsp; Wednesday, June 05, 2013 at 10:00 AM EDT</div>
</article>

<article class="abs card" style="left:116px;top:724px">
  <div class="head">HALDEN WELLNESS CENTER IN ASHGROVE, GA</div>
  <div class="thumb" role="img" aria-label="Large two-story house with lawn"></div>
  <div class="title">Corwin Tate Auctions, LLC GAL 5812 - Everything sold to the high bidder</div>
  <div class="info">Location:<br>Location 1 - 418 Maple Ridge Rd<br>Location 2 - 52 Cedar Hollow # 3<br>Ashgrove, GA 30999</div>
  <div class="details"><svg width="24" height="24" viewBox="0 0 24 24"><rect x="1" y="1" width="17" height="20" rx="2" fill="#fff"/><circle cx="10" cy="11" r="5" fill="none" stroke="#b5604a" stroke-width="2"/><path d="M14 15l7 7" stroke="#fff" stroke-width="3"/></svg>DETAILS</div>
  <div class="bid"><b>Online Bidding Only</b><br>Began:&nbsp; Friday, May 24, 2013 at 10:06 AM EDT<br>Ends:&nbsp; Wednesday, June 05, 2013 at 10:00 AM EDT</div>
</article>

<aside class="abs register">
  <h2>REGISTER TO BID</h2>
  <p>Find great deals at our online<br>auctions</p>
  <div class="art" role="img" aria-label="Bid lettering with a computer mouse"></div>
</aside>

<div class="abs house-box"><div class="img" role="img" aria-label="Two-story suburban house with double garage and palm trees"></div></div>

<section class="abs sms">
  <h2>SMS Sign Up</h2>
  <div class="field" style="left:13px;top:44px;width:245px;height:34px">Enter your email</div>
  <div class="field" style="left:13px;top:93px;width:245px;height:34px">Enter your phone number</div>
  <div class="btn-dark" style="left:62px;top:140px;width:151px;height:37px">
    <svg width="26" height="26" viewBox="0 0 26 26"><rect x="9" y="6" width="11" height="18" rx="2" fill="none" stroke="#fff" stroke-width="2"/><ellipse cx="8" cy="7" rx="7" ry="5" fill="#fff"/><text x="8" y="9" font-size="5" text-anchor="middle" fill="#111" font-family="Arimo,sans-serif">SMS</text></svg>Sign Up
  </div>
</section>

<footer class="abs footer">
  <div class="flogo"><div class="mark"></div><span>Millbrook Auctions</span></div>
  <div class="links">Home<i>|</i>Auctions<i>|</i>Online Auctions<i>|</i>Past Auctions<i>|</i>About Us<i>|</i>FAQ<i>|</i>Blog<i>|</i>Contact Us</div>
  <div class="line" style="top:54px">Phone: 555- 014-2290, Email: info@millbrookauctions.example</div>
  <div class="line" style="top:78px">Copyright&nbsp; Millbrook Auction 2013 - 2014 .&nbsp; All Rights Reserved</div>
</footer>
</body>
</html>
```